Mobile App UI for Telecommunications/Hosting Company

We are about to convert our existing self-service Customer Portal into a mobile phone application and need an elegant and professional UI/UX design. Our company provides telecommunication (voice/mobile/data) and hosting services to medium-sized business. The primary purpose of the application is to view trouble tickets, alerts, orders, and performance charts. This application is available to customers only - not the general public.

Please provide a UI design suitable for display on iPhone/Android devices. The attached document includes a proposed screen flow. You are free to design your own screens to display the same information elegantly.
Updates

Please note that the design should be based on the wireframes in the Word document, not the screenshots.  The screenshots are just to show our existing web portal look & feel.

Also, just a few screens are required for initial submission (3 would be great).

Thanks,
Dermot.

Target Market(s)

IT Managers away from their desk and using a mobile phone application.
Adult males from technical background aged 30-50.
Customers of Brindlewood Networks have access to this application (not the general public). This is a self-service portal for customers only.

Industry/Entity Type

Business

Colors
0592cd
33a6d7
85cae6
cadf82
fde08a

Requirements
Must have
• Please look at the screenshots from our current Customer Portal site (part of the project brief). The mobile app does not have to look the same, but should follow a similar style.

Please check out our company web site at www.brindlewoodnetworks.example (this site is not the customer portal and has a different look at feel) to understand what Brindlewood Networks does.
Nice to have
• Sharing capabilities via email/SMS.
A nice background image to make it stand out
The colours selected below are a guide only as they are similar to the corporate colours
- The priority is something that works on a phone - a design extendable to tablets is a nice to have as our existing web site looks OK on a tablet..

```html
<!DOCTYPE html>
<html lang="en">
<head>
<meta charset="utf-8">
<title>Brindlewood Networks – Customer Portal App Screens</title>
<link rel="stylesheet" href="https://fonts.googleapis.com/css2?family=Raleway:wght@300;400;500;600;700&family=Comfortaa:wght@300;400&family=Arimo:wght@400;700&display=swap">
<style>
:root{
  --page:#eeeeee;
  --blue-bright:#33a6d7;
  --blue-core:#0592cd;
  --blue-light:#85cae6;
  --header-top:#0c6a98;
  --header-bottom:#2b8cbc;
  --band-event:#0e6896;
  --band-recent:#053b5c;
  --date-tile:#3a9fd2;
  --news-title:#33a6d7;
  --news-text:#7fb6cf;
  --item-title:#0b5f8e;
  --item-text:#5f8fab;
  --row-alt:#f5f6f7;
  --row-line:#e3e6e8;
  --tabbar:#3b3b3b;
  --tab-icon:#d8d8d8;
  --white:#ffffff;
  --input-bg:#0a6fa3;
  --input-line:#07557f;
}
*{box-sizing:border-box;margin:0;padding:0}
html,body{width:1200px;height:1190px;overflow:hidden;background:var(--page)}
body{position:relative;font-family:"Raleway",sans-serif}

.screen{position:absolute;top:221px;width:392px;height:696px;overflow:hidden}
.screen--login{left:118px;background:radial-gradient(ellipse 70% 45% at 50% 33%,#8fd2ef 0%,#3aa9db 35%,var(--blue-core) 75%,#0686c2 100%)}
.screen--home{left:648px;background:var(--white)}

.status-bar{position:absolute;top:0;left:0;right:0;height:26px;color:var(--white);font-family:"Arimo",sans-serif;font-size:15px}
.status-bar .carrier{position:absolute;left:6px;top:5px;display:flex;align-items:center;gap:6px}
.status-bar .time{position:absolute;left:0;right:0;top:4px;text-align:center}
.status-bar .battery{position:absolute;right:8px;top:5px;display:flex;align-items:center;gap:6px}

/* login */
.brand-name{position:absolute;left:0;right:0;top:292px;text-align:center;color:var(--white);font-size:30px;font-weight:400;letter-spacing:.3px}

.login-form{position:absolute;left:71px;top:378px;width:250px}
.field{height:40px;background:var(--input-bg);border:1px solid var(--input-line);margin-bottom:5px;position:relative;color:#9fcde4;font-size:11px;padding:12px 0 0 9px}
.field svg{position:absolute;right:10px;top:10px}
.remember{color:var(--white);font-size:11px;display:flex;align-items:center;gap:4px;margin-top:11px}
.remember svg{display:block}
.login-btn{margin-top:24px;height:40px;background:linear-gradient(#b8e2f5,#8ccde9);color:var(--input-line);text-align:center;font-size:19px;line-height:40px;font-weight:500}

/* home */
.app-header{position:absolute;top:0;left:0;right:0;height:80px;background:linear-gradient(var(--header-top),var(--header-bottom));border-bottom:2px solid #9ac9e0}
.app-header .brand-title{position:absolute;left:0;right:0;top:38px;text-align:center;color:var(--white);font-size:18px;font-weight:400}

.news{position:absolute;top:80px;left:0;right:0;height:136px;padding:10px 14px 0 18px}
.news h2{color:var(--news-title);font-size:23px;font-weight:700}
.news p{color:var(--news-text);font-size:12px;line-height:15px;margin-top:3px;font-weight:500}

.band{position:absolute;left:0;right:0;height:65px;color:var(--white);font-family:"Comfortaa",sans-serif;font-size:21px;display:flex;align-items:center;gap:9px;padding-left:18px}
.band--event{top:216px;background:var(--band-event)}
.band--recent{top:449px;background:var(--band-recent)}

.feed-row{position:absolute;left:0;right:0;height:84px;background:var(--white);border-bottom:1px solid var(--row-line)}
.feed-row--alt{background:var(--row-alt)}
.date-tile{position:absolute;left:0;top:0;width:72px;height:100%;background:var(--date-tile);color:var(--white);text-align:center;padding-top:12px;line-height:.95}
.date-tile .day{font-size:28px;font-weight:300;display:block}
.date-tile .rest{font-size:14px;font-weight:400}
.row-text{position:absolute;top:15px;right:50px}
.row-text h3{color:var(--item-title);font-size:14px;font-weight:600}
.row-text p{color:var(--item-text);font-size:12.5px;line-height:15px;margin-top:5px;font-weight:500}
.chevron{position:absolute;right:20px;top:34px}

.tab-bar{position:absolute;left:0;right:0;bottom:0;height:60px;background:var(--tabbar);display:flex}
.tab-bar .tab{flex:1;display:flex;align-items:center;justify-content:center;border-right:1px solid #2e2e2e}
.tab-bar .tab:last-child{border-right:0}
</style>
</head>
<body>

<section class="screen screen--login" aria-label="Login screen">
  <div class="status-bar">
    <span class="carrier">●●●●● Nordcell
      <svg width="14" height="11" viewBox="0 0 14 11"><path d="M1 4a9 9 0 0 1 12 0M3 6.5a6 6 0 0 1 8 0M5 9a3 3 0 0 1 4 0" stroke="#fff" stroke-width="1.4" fill="none"/></svg></span>
    <span class="time">9:25 PM</span>
    <span class="battery">100% <svg width="30" height="12" viewBox="0 0 30 12"><rect x=".5" y=".5" width="26" height="11" fill="none" stroke="#fff"/><rect x="2" y="2" width="23" height="8" fill="#fff"/><rect x="27" y="4" width="2" height="4" fill="#fff"/></svg></span>
  </div>

  <div class="brand-name">Brindlewood Networks</div>

  <form class="login-form">
    <div class="field">Username
      <svg width="18" height="20" viewBox="0 0 18 20"><circle cx="9" cy="6" r="4.5" fill="none" stroke="#6fb3d6" stroke-width="1.2"/><path d="M1.5 19c0-5 3-7.5 7.5-7.5s7.5 2.5 7.5 7.5z" fill="none" stroke="#6fb3d6" stroke-width="1.2"/></svg></div>
    <div class="field">Password
      <svg width="16" height="20" viewBox="0 0 16 20"><path d="M4 9V6a4 4 0 0 1 8 0v3" fill="none" stroke="#6fb3d6" stroke-width="1.2"/><rect x="1.5" y="9" width="13" height="10" rx="1" fill="none" stroke="#6fb3d6" stroke-width="1.2"/><circle cx="8" cy="14" r="1.3" fill="#6fb3d6"/></svg></div>
    <label class="remember"><svg width="13" height="13" viewBox="0 0 13 13"><rect x=".5" y=".5" width="12" height="12" fill="#1a8cc4" stroke="#8fd0ec"/><path d="M3 6.5l2.5 2.5L10.5 3.5" fill="none" stroke="#fff" stroke-width="1.4"/></svg>Remember me!</label>
    <div class="login-btn">LOGIN</div>
  </form>
</section>

<section class="screen screen--home" aria-label="Home screen">
  <header class="app-header">
    <div class="status-bar">
      <span class="carrier">●●●●● Nordcell
        <svg width="14" height="11" viewBox="0 0 14 11"><path d="M1 4a9 9 0 0 1 12 0M3 6.5a6 6 0 0 1 8 0M5 9a3 3 0 0 1 4 0" stroke="#fff" stroke-width="1.4" fill="none"/></svg></span>
      <span class="time">9:25 PM</span>
      <span class="battery">100% <svg width="30" height="12" viewBox="0 0 30 12"><rect x=".5" y=".5" width="26" height="11" fill="none" stroke="#fff"/><rect x="2" y="2" width="23" height="8" fill="#fff"/><rect x="27" y="4" width="2" height="4" fill="#fff"/></svg></span>
    </div>
    <div class="brand-title">Brindlewood Networks</div>
  </header>

  <article class="news">
    <h2>News</h2>
    <p>Lorem ipsum dolor sit amet, consectetuer adipiscing elit, sed diam nonummy nibh euismod tincidunt ut laoreet dolore magna aliquam erat volutpat. Ut wisi enim ad minim veniam, quis nostrud exerci tation ullamcorper suscipit lobortis nisl ut aliquip ex ea commodo consequat.</p>
  </article>

  <div class="band band--event">
    <svg width="32" height="30" viewBox="0 0 32 30"><rect x="1.5" y="4" width="29" height="24.5" fill="none" stroke="#fff" stroke-width="2"/><line x1="1.5" y1="10" x2="30.5" y2="10" stroke="#fff" stroke-width="2"/><line x1="8" y1="1" x2="8" y2="7" stroke="#fff" stroke-width="2"/><line x1="24" y1="1" x2="24" y2="7" stroke="#fff" stroke-width="2"/><text x="16" y="25" text-anchor="middle" fill="#fff" font-family="Arimo,sans-serif" font-size="12" font-weight="700">24</text></svg>
    Event Feed
  </div>

  <div class="feed-row feed-row--alt" style="top:281px">
    <div class="date-tile"><span class="day">28</span><span class="rest">MAR<br>2014</span></div>
    <div class="row-text" style="left:86px"><h3>Lorem ipsum dolor sit amet</h3><p>Lorem ipsum dolor sit amet, consectetuer adipiscing elit, sed diam nonummy</p></div>
    <svg class="chevron" width="10" height="16" viewBox="0 0 10 16"><path d="M2 2l6 6-6 6" fill="none" stroke="#9aa4aa" stroke-width="2"/></svg>
  </div>
  <div class="feed-row" style="top:365px">
    <div class="date-tile"><span class="day">28</span><span class="rest">MAR<br>2014</span></div>
    <div class="row-text" style="left:86px"><h3>Lorem ipsum dolor sit amet</h3><p>Lorem ipsum dolor sit amet, consectetuer adipiscing elit, sed diam nonummy</p></div>
    <svg class="chevron" width="10" height="16" viewBox="0 0 10 16"><path d="M2 2l6 6-6 6" fill="none" stroke="#9aa4aa" stroke-width="2"/></svg>
  </div>

  <div class="band band--recent">
    <svg width="32" height="30" viewBox="0 0 32 30"><rect x="1.5" y="4" width="29" height="24.5" fill="none" stroke="#fff" stroke-width="2"/><line x1="1.5" y1="10" x2="30.5" y2="10" stroke="#fff" stroke-width="2"/><line x1="8" y1="1" x2="8" y2="7" stroke="#fff" stroke-width="2"/><line x1="24" y1="1" x2="24" y2="7" stroke="#fff" stroke-width="2"/><text x="16" y="25" text-anchor="middle" fill="#fff" font-family="Arimo,sans-serif" font-size="12" font-weight="700">24</text></svg>
    Recently Accessed
  </div>

  <div class="feed-row feed-row--alt" style="top:514px;height:85px">
    <div class="row-text" style="left:19px"><h3>Lorem ipsum dolor sit amet</h3><p>Lorem ipsum dolor sit amet, consectetuer<br>adipiscing elit, sed diam nonummy</p></div>
    <svg class="chevron" width="10" height="16" viewBox="0 0 10 16"><path d="M2 2l6 6-6 6" fill="none" stroke="#9aa4aa" stroke-width="2"/></svg>
  </div>
  <div class="feed-row" style="top:599px;height:85px">
    <div class="row-text" style="left:19px"><h3>Lorem ipsum dolor sit amet</h3></div>
  </div>

  <nav class="tab-bar" aria-label="Main navigation">
    <div class="tab"><svg width="30" height="30" viewBox="0 0 30 30"><path d="M17 4l9 9-13 13-9-9V8l4-4z" fill="none" stroke="var(--tab-icon)" stroke-width="1.8" transform="rotate(10 15 15)"/><circle cx="10" cy="10" r="1.8" fill="var(--tab-icon)"/></svg></div>
    <div class="tab"><svg width="30" height="30" viewBox="0 0 30 30"><path d="M7 22h16l-2-3v-6a6 6 0 0 0-12 0v6z" fill="none" stroke="var(--tab-icon)" stroke-width="1.8"/><path d="M12.5 25a2.5 2.5 0 0 0 5 0" fill="none" stroke="var(--tab-icon)" stroke-width="1.8"/><line x1="15" y1="4" x2="15" y2="7" stroke="var(--tab-icon)" stroke-width="1.8"/></svg></div>
    <div class="tab"><svg width="30" height="30" viewBox="0 0 30 30"><path d="M3 6h4l3 12h13l3-9H9" fill="none" stroke="var(--tab-icon)" stroke-width="1.8"/><circle cx="12" cy="23" r="1.8" fill="var(--tab-icon)"/><circle cx="21" cy="23" r="1.8" fill="var(--tab-icon)"/></svg></div>
    <div class="tab"><svg width="30" height="30" viewBox="0 0 30 30"><circle cx="15" cy="15" r="4" fill="none" stroke="var(--tab-icon)" stroke-width="1.8"/><circle cx="15" cy="15" r="9" fill="none" stroke="var(--tab-icon)" stroke-width="3.5" stroke-dasharray="3.5 3.6"/><circle cx="15" cy="15" r="7.5" fill="none" stroke="var(--tab-icon)" stroke-width="1.6"/></svg></div>
    <div class="tab"><svg width="30" height="30" viewBox="0 0 30 30"><rect x="7" y="3" width="18" height="24" rx="1.5" fill="none" stroke="var(--tab-icon)" stroke-width="1.8"/><line x1="5" y1="9" x2="9" y2="9" stroke="var(--tab-icon)" stroke-width="1.8"/><line x1="5" y1="15" x2="9" y2="15" stroke="var(--tab-icon)" stroke-width="1.8"/><line x1="5" y1="21" x2="9" y2="21" stroke="var(--tab-icon)" stroke-width="1.8"/><text x="16.5" y="19" text-anchor="middle" fill="var(--tab-icon)" font-family="Arimo,sans-serif" font-size="11">@</text></svg></div>
  </nav>
</section>

</body>
</html>
```